Cloud Hosting Provider Web Site

We need to create the design for Nimbo-Pails.net a new Cloud Hosting Provider Website.

We already have a logo and a draft website with preliminary content showing the desired structure for the final web site.

I need a design for the Home Page and all 10 Internal web pages currently linked from the draft home page.

The documentation site (/docs) Customer Portal (/portal) and Support site (/support) are not part of this design project.

We need images to illustrate all pages which of course need to be consistent with the content. Please read carefully the text of each page in the draft web site to understand the purpose of each page and illustrate it accordingly.

All pages must be illustrated with images, I do not want any single page with just text.

I want to maintain the slides idea of the draft website home page.

The web site must look professional, we are competitors of huge companies like tallow grid systems (tgs.tallowgrid.com), Velquist Oriel (oriel.velquist.com) and DuneLoft (www.duneloft.com) so we need to look as serious as them.

You may download the draft web site pages to style them, I need fully finalized HTML / CSS and image files.

A top link bar and link footer must be included in every page.

Also the web site will have the possibility to start a chat conversation with a sales agent, so a graphical link to do so must be included in the design, together with a chat window design (including HTML/CSS)

Information for accessing the draft web site follows:

URL: www.nimbo-pails.net
username: design
password: QOPqop987654

If you need any additional information please let me know.

```html
<!DOCTYPE html>
<html lang="en">
<head>
<meta charset="utf-8">
<title>Nimbo-Pails.net — The Cloud for Modern Business</title>
<link rel="stylesheet" href="https://fonts.googleapis.com/css2?family=Oswald:wght@400;500&family=Lato:wght@300;400;700&display=swap">
<style>
:root{
  --sky:#07a6e0;
  --sky-soft:#8fd4f0;
  --navy:#123e68;
  --ink:#1a1a1a;
  --muted:#a9a9a9;
  --teal:#17a8d6;
  --mint:#45d6a0;
  --indigo:#2f3f7a;
  --plum:#9b3aa0;
  --lemon:#eef27a;
  --lemon-soft:#f6f8b4;
  --pale:#ececec;
  --white:#ffffff;
}
*{box-sizing:border-box;margin:0;padding:0}
html,body{width:878px;height:1200px;overflow:hidden;background:var(--white)}
body{font-family:"Lato",sans-serif;color:var(--ink)}
.page{position:relative;width:878px;height:1200px;overflow:hidden}

/* header */
.brand{position:absolute;left:67px;top:84px;display:flex;align-items:center;gap:8px}
.brand-dot{width:18px;height:18px;border-radius:50%;background:var(--sky)}
.brand-name{font-weight:700;font-size:19px;color:var(--navy)}
.signup{position:absolute;left:661px;top:0;height:29px;width:145px;display:flex}
.signup-icon{width:35px;background:var(--lemon-soft);display:flex;align-items:center;justify-content:center}
.signup-label{flex:1;background:var(--lemon);font-family:"Oswald",sans-serif;font-size:14px;color:var(--navy);display:flex;align-items:center;justify-content:center;letter-spacing:.2px}
.nav{position:absolute;top:50px;left:306px;display:flex;align-items:center;font-size:11px;color:#222}
.nav a{color:inherit;text-decoration:none;height:25px;display:flex;align-items:center}
.nav .current{background:var(--sky);color:var(--white);padding:0 5px;margin-right:24px}
.nav .item{margin-right:28px}
.nav .item:last-child{margin-right:0}

/* hero */
.hero-sweep{position:absolute;left:0;top:118px}
.hero-ornament{position:absolute;left:576px;top:116px;width:302px;height:92px;background:linear-gradient(90deg,var(--sky),var(--sky-soft));border-radius:60px 60px 0 60px;opacity:.9}
.hero-visual{position:absolute;left:0;top:178px;width:354px;height:307px;border-radius:0 8px 0 0;background:linear-gradient(135deg,#0c1a3a,#071026 60%,#1b2b4a);border:4px solid #2a2a2a;border-left:0;border-bottom:0}
.hero-title{position:absolute;left:428px;top:226px;font-family:"Oswald",sans-serif;font-weight:500;font-size:47px;line-height:56px;background:linear-gradient(90deg,var(--teal),var(--mint));-webkit-background-clip:text;background-clip:text;color:transparent}
.hero-copy{position:absolute;left:429px;top:346px;width:390px;font-weight:300;font-size:13.6px;line-height:16.4px;color:var(--muted);white-space:nowrap}
.hero-btn{position:absolute;left:429px;top:406px;width:133px;height:31px;background:var(--pale);font-family:"Oswald",sans-serif;font-size:12.5px;color:var(--sky);display:flex;align-items:center;justify-content:center;letter-spacing:.6px}

/* band */
.band{position:absolute;left:0;top:485px;width:878px;height:70px;background:var(--sky)}
.band-text{position:absolute;left:113px;top:20px;font-weight:300;font-size:22px;color:var(--white)}
.band-btn{position:absolute;left:630px;top:21px;width:132px;height:31px;background:var(--white);font-family:"Oswald",sans-serif;font-size:12.5px;color:var(--sky);display:flex;align-items:center;justify-content:center;letter-spacing:.6px}

/* section titles */
.section-title{position:absolute;left:0;width:878px;text-align:center;font-family:"Oswald",sans-serif;font-weight:500;font-size:47px;line-height:60px}
.section-title span{background:linear-gradient(90deg,var(--indigo),var(--plum));-webkit-background-clip:text;background-clip:text;color:transparent}
.solutions-title{top:594px}
.divider{position:absolute;left:264px}
.solutions-divider{top:656px}

/* solutions */
.solution{position:absolute;top:732px;width:200px;text-align:center}
.solution-badge{margin:0 auto;width:124px;height:124px;border-radius:50%;background:var(--white);box-shadow:0 0 4px rgba(0,0,0,.25);display:flex;align-items:center;justify-content:center}
.solution-name{margin-top:20px;font-family:"Oswald",sans-serif;font-weight:400;font-size:20px;color:#111;letter-spacing:-.2px}
.solution-text{margin-top:4px;font-family:Arial,sans-serif;font-size:7.4px;line-height:11px;color:#333}
.solution-text b{color:#111}
.solution-btn{display:inline-block;margin-top:10px;height:21px;padding:0 11px;border-radius:4px;color:var(--white);font-size:9.5px;line-height:21px}
.btn-sky{background:var(--sky)}
.btn-navy{background:var(--navy)}
.pager{position:absolute;top:840px}

/* recommended */
.recommended{position:absolute;left:0;top:1026px;width:878px;height:174px;background:linear-gradient(160deg,#a64fa9,#9c3f9f 50%,#a54ba7)}
.recommended-title{top:1052px}
.recommended-title span{background:linear-gradient(90deg,#ffffff,#f3f06a);-webkit-background-clip:text;background-clip:text;color:transparent}
.recommended-divider{top:1115px}
</style>
</head>
<body>
<div class="page">

  <header>
    <div class="brand"><span class="brand-dot"></span><span class="brand-name">Nimbo-Pails.net</span></div>
    <div class="signup">
      <div class="signup-icon">
        <svg width="16" height="16" viewBox="0 0 16 16"><circle cx="8" cy="5" r="3.6" fill="#111"/><path d="M1 16c0-4 3-6.5 7-6.5s7 2.5 7 6.5z" fill="#111"/></svg>
      </div>
      <div class="signup-label">+ SIGN UP NOW!</div>
    </div>
    <nav class="nav">
      <a class="current">HOME</a>
      <a class="item">USE CASES</a>
      <a class="item">CLOUD SERVICES</a>
      <a class="item">PAIL'S INFRASTRUCTURE</a>
      <a class="item">OUR COMPANY</a>
    </nav>
  </header>

  <section class="hero">
    <svg class="hero-sweep" width="878" height="40" viewBox="0 0 878 40"><path d="M0 12 Q300 0 600 8 L600 20 Q300 10 0 22z" fill="#f1f1f1"/></svg>
    <div class="hero-ornament" role="img" aria-label="Decorative blue cloud with lightning bolts"></div>
    <div class="hero-visual" role="img" aria-label="Monitor displaying a financial candlestick chart"></div>
    <h1 class="hero-title">THE CLOUD FOR<br>MODERN BUSINESS</h1>
    <p class="hero-copy">Experience our highly specialized expertise and best-in-class<br>service across the world's leading infrastructure technologies,<br>databases, and applications.</p>
    <div class="hero-btn">READ MORE</div>
  </section>

  <section class="band">
    <div class="band-text">Broad &amp; Deep Core Cloud Infrastructure Services</div>
    <div class="band-btn">CONTACT US</div>
  </section>

  <section class="solutions">
    <h2 class="section-title solutions-title"><span>POPULAR SOLUTIONS</span></h2>
    <svg class="divider solutions-divider" width="352" height="16" viewBox="0 0 352 16">
      <defs><linearGradient id="lineA" x1="0" x2="1"><stop offset="0" stop-color="#c8c8d8" stop-opacity="0"/><stop offset=".5" stop-color="#6a6a90"/><stop offset="1" stop-color="#c8c8d8" stop-opacity="0"/></linearGradient></defs>
      <rect x="0" y="7.5" width="352" height="1" fill="url(#lineA)"/>
      <path d="M176 1 L183 8 L176 15 L169 8z" fill="#5a4a8a"/>
    </svg>

    <svg class="pager" style="left:68px" width="20" height="30" viewBox="0 0 20 30"><path d="M16 2 L4 15 L16 28" fill="none" stroke="#a8a8a8" stroke-width="5"/></svg>
    <svg class="pager" style="left:788px" width="20" height="30" viewBox="0 0 20 30"><path d="M4 2 L16 15 L4 28" fill="none" stroke="#a8a8a8" stroke-width="5"/></svg>

    <article class="solution" style="left:91px">
      <div class="solution-badge">
        <svg width="108" height="108" viewBox="0 0 108 108"><circle cx="54" cy="54" r="54" fill="#07a6e0"/>
          <path d="M30 66 Q18 64 20 52 Q22 42 33 42 Q36 28 52 28 Q68 28 72 40 Q88 38 88 53 Q88 66 76 66" fill="none" stroke="#fff" stroke-width="7" stroke-linejoin="round"/>
          <rect x="49" y="46" width="10" height="26" fill="#fff"/><path d="M40 68 L68 68 L54 84z" fill="#fff"/></svg>
      </div>
      <h3 class="solution-name">Private Cloud</h3>
      <p class="solution-text">Lorem ipsum dolor sit amet, consectetuer<br>adipiscing elit, euismod tincidunt ut laoreet<br>dolore <b>magna aliquam erat volutpat.</b></p>
      <span class="solution-btn btn-sky">Read More</span>
    </article>

    <article class="solution" style="left:336px">
      <div class="solution-badge">
        <svg width="108" height="108" viewBox="0 0 108 108"><circle cx="54" cy="54" r="54" fill="#123e68"/>
          <rect x="24" y="28" width="60" height="6" fill="#fff"/><rect x="30" y="34" width="48" height="34" fill="none" stroke="#fff" stroke-width="4"/>
          <path d="M38 60 L48 50 L56 54 L68 42" fill="none" stroke="#fff" stroke-width="3"/>
          <path d="M54 68 V86 M54 72 L36 86 M54 72 L72 86" stroke="#fff" stroke-width="3"/></svg>
      </div>
      <h3 class="solution-name">Start Your Business</h3>
      <p class="solution-text">Lorem ipsum dolor sit amet, consectetuer<br>adipiscing elit, euismod tincidunt ut laoreet<br>dolore <b>magna aliquam erat volutpat.</b></p>
      <span class="solution-btn btn-navy">Read More</span>
    </article>

    <article class="solution" style="left:580px">
      <div class="solution-badge">
        <svg width="108" height="108" viewBox="0 0 108 108"><circle cx="54" cy="54" r="54" fill="#07a6e0"/>
          <circle cx="54" cy="56" r="32" fill="none" stroke="#fff" stroke-width="7"/>
          <circle cx="54" cy="56" r="18" fill="none" stroke="#fff" stroke-width="6"/>
          <circle cx="54" cy="56" r="5" fill="#fff"/>
          <path d="M54 56 L82 26" stroke="#fff" stroke-width="5"/></svg>
      </div>
      <h3 class="solution-name">Cloud Services</h3>
      <p class="solution-text">Lorem ipsum dolor sit amet, consectetuer<br>adipiscing elit, euismod tincidunt ut laoreet<br>dolore <b>magna aliquam erat volutpat.</b></p>
      <span class="solution-btn btn-sky">Read More</span>
    </article>
  </section>

  <section class="recommended" role="img" aria-label="Purple faceted background"></section>
  <h2 class="section-title recommended-title"><span>RECOMMENDED FOR YOU</span></h2>
  <svg class="divider recommended-divider" width="352" height="16" viewBox="0 0 352 16">
    <defs><linearGradient id="lineB" x1="0" x2="1"><stop offset="0" stop-color="#fff" stop-opacity="0"/><stop offset=".5" stop-color="#fff" stop-opacity=".8"/><stop offset="1" stop-color="#fff" stop-opacity="0"/></linearGradient></defs>
    <rect x="0" y="7.5" width="352" height="1" fill="url(#lineB)"/>
    <path d="M176 1 L183 8 L176 15 L169 8z" fill="#f2f2f2"/>
  </svg>

</div>
</body>
</html>
```